custom carpentry, woodworking and home repair company needs logo design and business card design

Attention: I apologize but I just received notification from my state that I cannot use the company name that I originally submitted (Beyond The Bench). The new name will be Joinolux We need a company logo and business card design for our new company based in the Hampton Roads area of Virginia. The company name is Joinolux. The final design should give a first impression of true craftsmanship and attention to detail. We would like the card to include the company name, my name Mark Tellman (owner), phone number (757) 348-2615, website (joinolux-example.com) and email address (mark@joinolux-example.com). Everything else is up to your discretion. Thanks, have fun, and good luck.

Industry/Entity Type

Business

Contact Information for Business Card

See project description

Logo Text

see project description

Colors

Designer to choose colors to be used in the design.

```html
<!DOCTYPE html>
<html lang="en">
<head>
<meta charset="utf-8">
<title>Joinolux Business Card</title>
<link rel="stylesheet" href="https://fonts.googleapis.com/css2?family=Arvo:wght@400;700&display=swap">
<style>
  :root {
    --page-bg: #ffffff;
    --wood-dark: #3b2210;
    --wood-mid: #7a4a22;
    --wood-light: #a8703a;
    --ink: #000000;
    --paper: #ffffff;
    --card-edge: #d9d9d9;
  }
  * { margin: 0; padding: 0; box-sizing: border-box; }
  html, body {
    width: 1200px;
    height: 1179px;
    overflow: hidden;
    background: var(--page-bg);
    font-family: "Arvo", "Rockwell", serif;
    color: var(--ink);
  }
  .sheet {
    width: 1200px;
    height: 1179px;
    display: flex;
    flex-direction: column;
    align-items: center;
    justify-content: center;
    gap: 22px;
  }
  .card {
    position: relative;
    width: 960px;
    height: 549px;
    overflow: hidden;
  }
  /* Front */
  .card-front {
    display: flex;
    align-items: center;
    justify-content: center;
  }
  .wood-photo {
    position: absolute;
    inset: 0;
    background: linear-gradient(180deg, var(--wood-mid) 0%, var(--wood-light) 35%, var(--wood-mid) 68%, var(--wood-dark) 72%, var(--wood-mid) 78%, var(--wood-light) 100%);
  }
  .front-logo {
    position: relative;
    margin-top: -44px;
    font-weight: 400;
    font-size: 150px;
    letter-spacing: 2px;
    color: var(--paper);
    line-height: 1;
  }
  /* Back */
  .card-back {
    background: var(--paper);
    border: 1px solid var(--card-edge);
    text-align: center;
  }
  .back-logo {
    position: absolute;
    top: 52px;
    left: 0;
    right: 0;
    font-size: 82px;
    font-weight: 400;
    letter-spacing: 1px;
    line-height: 1;
  }
  .contact {
    position: absolute;
    top: 180px;
    left: 0;
    right: 0;
  }
  .contact-name {
    font-size: 33px;
    line-height: 1.05;
    text-transform: uppercase;
  }
  .contact-role {
    font-size: 25px;
    line-height: 1.1;
  }
  .contact-phone {
    margin-top: 18px;
    font-size: 31px;
    line-height: 1.2;
  }
  .contact-email {
    font-size: 28px;
    font-weight: 700;
    line-height: 1.2;
  }
  .footer-band {
    position: absolute;
    left: 0;
    right: 0;
    bottom: 0;
    height: 146px;
    background: var(--ink);
    color: var(--paper);
    padding-top: 26px;
  }
  .footer-site {
    font-size: 34px;
    font-weight: 700;
    line-height: 1.15;
  }
  .footer-services {
    font-size: 27px;
    line-height: 1.3;
  }
</style>
</head>
<body>
  <main class="sheet">
    <section class="card card-front">
      <div class="wood-photo" role="img" aria-label="Close-up photograph of weathered brown wood planks"></div>
      <h1 class="front-logo">Joinolux</h1>
    </section>

    <section class="card card-back">
      <h2 class="back-logo">Joinolux</h2>
      <div class="contact">
        <p class="contact-name">Mark Tellman</p>
        <p class="contact-role">owner</p>
        <p class="contact-phone">(757) 348-2615</p>
        <p class="contact-email">mark@joinolux-example.com</p>
      </div>
      <div class="footer-band">
        <p class="footer-site">joinolux-example.com</p>
        <p class="footer-services">custom carpentry • woodworking • home repairs</p>
      </div>
    </section>
  </main>
</body>
</html>
```